K9R Business Cards

Business Cards

Contact Information for Business Card

Company name, owner name, license #s, phone & email

Requirements
Should not have
• mailing address

```html
<!DOCTYPE html>
<html lang="en">
<head>
<meta charset="UTF-8">
<title>K9R Business Cards</title>
<link href="https://fonts.googleapis.com/css2?family=Open+Sans:wght@400;600;700;800&display=swap" rel="stylesheet">
<style>
  :root {
    --stage: #a6a6a6;
    --card-dark: #232327;
    --card-dark-tone: #2e2e33;
    --card-light: #ffffff;
    --brand-blue: #233f94;
    --brand-red: #c1272d;
    --ink: #111111;
  }
  * { margin: 0; padding: 0; box-sizing: border-box; }
  html, body { width: 1200px; height: 780px; overflow: hidden; }
  body {
    background: var(--stage);
    font-family: "Open Sans", Arial, sans-serif;
    position: relative;
  }
  .card {
    position: absolute;
    left: 320px;
    width: 561px;
    height: 321px;
    overflow: hidden;
  }
  .card--back { top: 53px; background: var(--card-dark); }
  .card--front { top: 406px; background: var(--card-light); }

  .back-pattern {
    position: absolute; inset: 0;
    background: linear-gradient(160deg, var(--card-dark-tone), var(--card-dark));
  }
  .back-brand {
    position: absolute;
    left: 404px; top: 236px;
    width: 84px;
    text-align: center;
    color: #ffffff;
    font-weight: 700;
    font-size: 13px;
    letter-spacing: 2px;
    line-height: 1.2;
  }

  .front-brand {
    position: absolute;
    left: 0; right: 0; top: 40px;
    text-align: center;
  }
  .front-brand__name {
    display: block;
    color: var(--brand-blue);
    font-weight: 800;
    font-size: 78px;
    line-height: 80px;
    letter-spacing: 2px;
  }
  .front-brand__trade {
    display: block;
    color: var(--ink);
    font-weight: 700;
    font-size: 30px;
    line-height: 34px;
    margin-top: 2px;
  }

  .owner {
    position: absolute;
    left: 44px; top: 218px;
    width: 222px;
    text-align: left;
    white-space: nowrap;
  }
  .owner__name {
    font-weight: 700;
    font-size: 27px;
    line-height: 34px;
    color: var(--brand-blue);
  }
  .owner__name .surname { color: var(--brand-red); }
  .owner__license {
    font-size: 16px;
    line-height: 22px;
    color: var(--ink);
  }
  .owner__license .label { color: var(--brand-red); }

  .divider {
    position: absolute;
    left: 280px; top: 202px;
    width: 1px; height: 90px;
    background: var(--ink);
  }

  .contact {
    position: absolute;
    left: 319px; top: 227px;
    list-style: none;
    white-space: nowrap;
  }
  .contact__item {
    display: flex;
    align-items: center;
    gap: 8px;
    font-size: 15px;
    line-height: 19px;
    color: var(--ink);
  }
  .contact__icon { width: 13px; height: 13px; flex: none; }
</style>
</head>
<body>

  <section class="card card--back">
    <div class="back-pattern" role="img" aria-label="Dark background with a repeated embossed brand-name pattern"></div>
    <div class="back-brand">K9R REALTY</div>
  </section>

  <section class="card card--front">
    <header class="front-brand">
      <span class="front-brand__name">K9R</span>
      <span class="front-brand__trade">CONSTRUCTION</span>
    </header>

    <div class="owner">
      <p class="owner__name">Dana <span class="surname">Holloway</span></p>
      <p class="owner__license"><span class="label">MN License #</span> BC482157</p>
    </div>

    <div class="divider"></div>

    <ul class="contact">
      <li class="contact__item">
        <svg class="contact__icon" viewBox="0 0 24 24" aria-hidden="true">
          <path fill="#c1272d" d="M6.6 10.8a15.2 15.2 0 0 0 6.6 6.6l2.2-2.2a1 1 0 0 1 1-.25 11.4 11.4 0 0 0 3.6.57 1 1 0 0 1 1 1V20a1 1 0 0 1-1 1A17 17 0 0 1 3 4a1 1 0 0 1 1-1h3.5a1 1 0 0 1 1 1c0 1.25.2 2.45.57 3.570a1 1 0 0 1-.25 1z"/>
        </svg>
        <span>612-555-0148</span>
      </li>
      <li class="contact__item">
        <svg class="contact__icon" viewBox="0 0 24 24" aria-hidden="true">
          <rect x="2" y="6" width="20" height="14" rx="1" fill="#233f94"/>
          <path d="M2 7l10 7 10-7" fill="none" stroke="#ffffff" stroke-width="1.6"/>
        </svg>
        <span>danaholloway@mail.com</span>
      </li>
    </ul>
  </section>

</body>
</html>
```